Profesional personal website needs design and business card

I need a business card with my professional name as a logo "Orlan Vitality" for my business. I am a Wellness Coach, consultant and trainer. So it should be professional, wellness oriented and modern.

Target Market(s)

Private clients, governments, corporations. Luxury and high market.

Industry/Entity Type

Health And Wellness

Contact Information for Business Card

Orlan Vitality should be the logo

Colors

Designer to choose colors to be used in the design.

Requirements
Must have
• Orlan Vitality
• Name: Dario Montalbe
• Wellness Coach, Consultant & Trainer.
• Website: www.orlanvitality-example.com
• Phone:
• Spain (+34) 612 480 597
• (USA) +1 (555) 318 0264
Nice to have
• The most important is the design of "Orlan Vitality", as this is going to be my personal brand logo. It should be professional, wellness, high end and actual.
Should not have
• no golds, no baroque style..

```html
<!DOCTYPE html>
<html lang="en">
<head>
<meta charset="utf-8">
<title>Orlan Vitality – Business Card</title>
<link rel="stylesheet" href="https://fonts.googleapis.com/css2?family=Poppins:wght@300;400;600;700&display=swap">
<style>
  :root {
    --page-bg: #1e1e1e;
    --card-white: #ffffff;
    --brand-green: #349a32;
    --ink: #3a3a3a;
    --ink-soft: #4a4a4a;
    --on-green: #ffffff;
  }
  * { box-sizing: border-box; margin: 0; padding: 0; }
  html, body {
    width: 1200px; height: 904px; overflow: hidden;
    background: var(--page-bg);
    font-family: "Poppins", sans-serif;
  }
  .sheet {
    width: 1200px; height: 904px;
    display: flex; flex-direction: column; align-items: center; justify-content: center;
    gap: 36px;
  }
  .card {
    width: 700px; height: 400px; position: relative; overflow: hidden;
  }

  /* Front */
  .card--front { background: var(--card-white); }
  .card--front .edge-band {
    position: absolute; left: 0; right: 0; bottom: 0; height: 14px;
    background: var(--brand-green);
  }
  .brand-name {
    font-family: "Poppins", sans-serif; font-weight: 400;
    letter-spacing: 0.02em; white-space: nowrap;
  }
  .card--front .brand-name {
    position: absolute; left: 40px; top: 180px; width: 290px; text-align: center;
    font-size: 30px; color: var(--brand-green);
  }
  .card--front .divider {
    position: absolute; left: 355px; top: 95px; width: 2px; height: 200px;
    background: var(--brand-green);
  }
  .contact-block { position: absolute; left: 392px; top: 118px; }
  .person-name { font-size: 32px; font-weight: 700; color: var(--ink); line-height: 1.1; }
  .person-title { font-size: 13px; font-weight: 400; color: var(--brand-green); margin-top: 4px; }
  .contact-list { list-style: none; margin-top: 22px; }
  .contact-list li {
    display: flex; align-items: center; gap: 12px;
    font-size: 14px; color: var(--ink-soft); line-height: 1; margin-bottom: 12px;
  }
  .contact-list svg { width: 16px; height: 16px; flex: none; }
  .contact-list .web { font-size: 13px; }
  .contact-list .web b { font-weight: 600; }

  /* Back */
  .card--back { background: var(--brand-green); color: var(--on-green); }
  .card--back .brand-name {
    position: absolute; left: 0; right: 0; top: 150px; text-align: center;
    font-size: 50px; color: var(--on-green);
  }
  .card--back .site {
    position: absolute; left: 0; right: 0; top: 300px; text-align: center;
    font-size: 20px; font-weight: 300; letter-spacing: 0.08em;
  }
  .card--back .site b { font-weight: 600; }
</style>
</head>
<body>
<main class="sheet">
  <section class="card card--front" aria-label="Business card front">
    <div class="brand-name">Orlan Vitality</div>
    <div class="divider"></div>
    <div class="contact-block">
      <h1 class="person-name">Dario Montalbe</h1>
      <p class="person-title">Wellness Coach, Consultant &amp; Trainer.</p>
      <ul class="contact-list">
        <li>
          <svg viewBox="0 0 24 24" aria-hidden="true"><path fill="#349a32" d="M6.6 10.8a15.1 15.1 0 0 0 6.6 6.6l2.2-2.2c.3-.3.7-.4 1-.2 1.1.4 2.3.6 3.6.6.6 0 1 .4 1 1V20c0 .6-.4 1-1 1A17 17 0 0 1 3 4c0-.6.4-1 1-1h3.5c.6 0 1 .4 1 1 0 1.3.2 2.5.6 3.6.1.3 0 .7-.2 1z"/></svg>
          <span>Spain (+34) 612 480 597</span>
        </li>
        <li>
          <svg viewBox="0 0 24 24" aria-hidden="true"><path fill="#349a32" d="M6.6 10.8a15.1 15.1 0 0 0 6.6 6.6l2.2-2.2c.3-.3.7-.4 1-.2 1.1.4 2.3.6 3.6.6.6 0 1 .4 1 1V20c0 .6-.4 1-1 1A17 17 0 0 1 3 4c0-.6.4-1 1-1h3.5c.6 0 1 .4 1 1 0 1.3.2 2.5.6 3.6.1.3 0 .7-.2 1z"/></svg>
          <span>(USA) +1 (555) 318 0264</span>
        </li>
        <li>
          <svg viewBox="0 0 24 24" aria-hidden="true"><g fill="none" stroke="#349a32" stroke-width="2"><circle cx="12" cy="12" r="9"/><ellipse cx="12" cy="12" rx="4" ry="9"/><path d="M3 12h18M5 7h14M5 17h14"/></g></svg>
          <span class="web">www.<b>orlanvitality-example</b>.com</span>
        </li>
      </ul>
    </div>
    <div class="edge-band"></div>
  </section>

  <section class="card card--back" aria-label="Business card back">
    <div class="brand-name">Orlan Vitality</div>
    <p class="site">www.<b>orlanvitality-example</b>.com</p>
  </section>
</main>
</body>
</html>
```